8.5 x 8.5 - HELOC Product Campaign

Home Equity Lines of Credit
are BACK!!!

* Up to 97.5% on Owner Occupied Properties
* 700 Minimum Scores
* Fund in only 2-3 weeks

Can be used for...
* Education Expense
* Bill Consolidation
* Home Improvement
* Investments

Call today for more information!
(800) 417-2960

Bluegate Lending Partners, Inc.
NMLS #381760
www.bluegatelendhub.com

```html
<!DOCTYPE html>
<html lang="en">
<head>
<meta charset="utf-8">
<title>HELOC Product Campaign – Bluegate Lending Partners</title>
<link rel="stylesheet" href="https://fonts.googleapis.com/css2?family=Oswald:wght@600;700&family=Montserrat:wght@500;600;700&display=swap">
<style>
  :root {
    --brand-blue: #0a5ea8;
    --olive: #a39b2c;
    --silver-light: #f2f2f2;
    --silver-mid: #c4c4c4;
    --ink: #2f2f2f;
    --white: #ffffff;
    --paper: #f4f5f6;
    --navy: #1c2740;
  }
  html, body {
    margin: 0;
    padding: 0;
    width: 1200px;
    height: 1200px;
    overflow: hidden;
    background: var(--white);
  }
  .flyer {
    position: relative;
    width: 1200px;
    height: 1200px;
    overflow: hidden;
    background: linear-gradient(180deg, var(--white) 0%, var(--paper) 100%);
    font-family: "Montserrat", Arial, sans-serif;
  }
  .flyer-art {
    position: absolute;
    inset: 0;
  }
  .headline {
    position: absolute;
    left: 62px;
    top: 50px;
    margin: 0;
    font-family: "Oswald", Impact, sans-serif;
    font-weight: 700;
    font-size: 78px;
    line-height: 91px;
    letter-spacing: 0.5px;
    color: var(--white);
    text-transform: uppercase;
  }
  .checklist {
    position: absolute;
    left: 62px;
    margin: 0;
    padding: 0;
    list-style: none;
    color: var(--white);
  }
  .checklist li {
    position: relative;
    padding-left: 40px;
    font-weight: 600;
    font-size: 22px;
  }
  .checklist li::before {
    content: "";
    position: absolute;
    left: 0;
    top: 6px;
    width: 17px;
    height: 17px;
    border-radius: 50%;
    background: var(--white);
  }
  .checklist li::after {
    content: "";
    position: absolute;
    left: 5px;
    top: 10px;
    width: 6px;
    height: 3px;
    border-left: 2px solid var(--olive);
    border-bottom: 2px solid var(--olive);
    transform: rotate(-45deg);
  }
  .checklist--features { top: 388px; }
  .checklist--features li { line-height: 32px; margin-bottom: 7px; }
  .checklist--uses { top: 664px; }
  .checklist--uses li { font-size: 23px; line-height: 32px; margin-bottom: 8px; }
  .checklist--uses li::after { border-color: var(--brand-blue); }
  .uses-title {
    position: absolute;
    left: 66px;
    top: 568px;
    margin: 0;
    font-family: "Oswald", Impact, sans-serif;
    font-weight: 600;
    font-size: 50px;
    line-height: 66px;
    color: var(--ink);
    text-transform: uppercase;
  }
  .cta-lead {
    position: absolute;
    left: 79px;
    top: 948px;
    margin: 0;
    font-weight: 600;
    font-size: 21px;
    color: var(--ink);
  }
  .phone-pill {
    position: absolute;
    left: 64px;
    top: 979px;
    width: 424px;
    height: 64px;
    border-radius: 32px;
    background: var(--brand-blue);
    display: flex;
    align-items: center;
    color: var(--white);
    font-weight: 700;
    font-size: 44px;
    letter-spacing: 0.5px;
  }
  .phone-icon {
    width: 44px;
    height: 44px;
    margin: 0 14px 0 10px;
    flex: none;
  }
  .company-block {
    position: absolute;
    left: 62px;
    top: 1068px;
    margin: 0;
    font-style: normal;
    font-weight: 600;
    font-size: 23px;
    line-height: 36px;
    color: var(--ink);
  }
  .company-block .company-name { color: var(--brand-blue); }
  .brand-mark {
    position: absolute;
    left: 790px;
    top: 1080px;
    width: 360px;
    display: flex;
    align-items: center;
    gap: 14px;
    font-weight: 700;
    font-size: 24px;
    line-height: 30px;
    color: var(--brand-blue);
  }
  .brand-mark .brand-dot {
    width: 44px;
    height: 44px;
    border-radius: 50%;
    background: var(--olive);
    flex: none;
  }
</style>
</head>
<body>
<main class="flyer">
  <svg class="flyer-art" width="1200" height="1200" viewBox="0 0 1200 1200">
    <defs>
      <linearGradient id="silverBand" x1="0" x2="1" y1="0" y2="0">
        <stop offset="0" stop-color="#d9d9d9"/>
        <stop offset="0.45" stop-color="#f2f2f2"/>
        <stop offset="1" stop-color="#bdbdbd"/>
      </linearGradient>
      <linearGradient id="roomTones" x1="0" x2="1" y1="0" y2="1">
        <stop offset="0" stop-color="#eceeef"/>
        <stop offset="0.55" stop-color="#cdb9a6"/>
        <stop offset="1" stop-color="#8c6a4c"/>
      </linearGradient>
      <linearGradient id="kitchenTones" x1="0" x2="1" y1="0" y2="1">
        <stop offset="0" stop-color="#e6e9ee"/>
        <stop offset="1" stop-color="#8da2bf"/>
      </linearGradient>
      <linearGradient id="billsTones" x1="0" x2="1" y1="0" y2="1">
        <stop offset="0" stop-color="#d6c3ae"/>
        <stop offset="1" stop-color="#3e4a66"/>
      </linearGradient>
      <linearGradient id="gradTones" x1="0" x2="0" y1="0" y2="1">
        <stop offset="0" stop-color="#8f8560"/>
        <stop offset="1" stop-color="#1f2a44"/>
      </linearGradient>
    </defs>

    <!-- blue backdrop -->
    <path class="backdrop-blue" fill="var(--brand-blue)"
      d="M0 0 H843 L640 230 L640 400 V560 H626 L340 860 Q280 920 217 919 Q90 915 0 786 Z"/>

    <!-- large living room photo -->
    <path role="img" aria-label="Photo: couple smiling at a tablet on a sofa among moving boxes"
      fill="url(#roomTones)"
      d="M843 0 H1200 V660 H990 L625 318 Q585 282 620 244 Z"/>

    <!-- thin white accent line -->
    <path class="accent-line" fill="none" stroke="var(--white)" stroke-width="2"
      d="M809 0 L630 181 Q562 250 594 358"/>

    <!-- olive feature band -->
    <rect class="band-olive" x="0" y="361" width="620" height="199" fill="var(--olive)"/>

    <!-- silver title band -->
    <polygon class="band-silver" points="0,562 495,562 462,641 0,641" fill="url(#silverBand)"/>

    <!-- diamond photo: kitchen planning -->
    <g class="photo-diamond" transform="rotate(45 730 479)">
      <rect x="570" y="319" width="320" height="320" rx="46" fill="var(--white)"/>
      <rect role="img" aria-label="Photo: couple reviewing renovation samples at a kitchen counter"
        x="578" y="327" width="304" height="304" rx="42" fill="url(#kitchenTones)"/>
      <rect x="592" y="341" width="276" height="276" rx="36" fill="none" stroke="var(--white)" stroke-width="2"/>
    </g>

    <!-- diamond photo: paying bills -->
    <g class="photo-diamond" transform="rotate(45 968 715)">
      <rect x="808" y="555" width="320" height="320" rx="46" fill="var(--white)"/>
      <rect role="img" aria-label="Photo: worried couple going over bills together"
        x="816" y="563" width="304" height="304" rx="42" fill="url(#billsTones)"/>
      <rect x="830" y="577" width="276" height="276" rx="36" fill="none" stroke="var(--white)" stroke-width="2"/>
    </g>

    <!-- diamond photo: graduate -->
    <g class="photo-diamond" transform="rotate(45 633 859)">
      <rect x="473" y="699" width="320" height="320" rx="46" fill="var(--navy)"/>
      <rect role="img" aria-label="Photo: smiling graduate in cap and gown"
        x="481" y="707" width="304" height="304" rx="42" fill="url(#gradTones)"/>
      <rect x="495" y="721" width="276" height="276" rx="36" fill="none" stroke="var(--white)" stroke-width="2"/>
    </g>
  </svg>

  <h1 class="headline">Home Equity<br>Lines of Credit<br>Are Back!!!</h1>

  <ul class="checklist checklist--features">
    <li>Up to 97.5% on Owner<br>Occupied Properties</li>
    <li>700 Minimum Scores</li>
    <li>Fund in only 2-3 weeks</li>
  </ul>

  <h2 class="uses-title">Can be used for</h2>

  <ul class="checklist checklist--uses">
    <li>Education Expense</li>
    <li>Bill Consolidation</li>
    <li>Home Improvement</li>
    <li>Investments</li>
  </ul>

  <p class="cta-lead">Call today for more information!</p>
  <div class="phone-pill">
    <svg class="phone-icon" viewBox="0 0 44 44" aria-hidden="true">
      <circle cx="22" cy="22" r="20" fill="var(--white)"/>
      <path d="M15 12 l5 0 l2 6 l-3 2 q2 5 7 7 l2 -3 l6 2 l0 5 q-2 2 -5 2 q-10 -2 -16 -16 q0 -3 2 -5 z"
        fill="var(--ink)"/>
    </svg>
    <span class="phone-number">(800) 417-2960</span>
  </div>

  <address class="company-block">
    <span class="company-name">Bluegate Lending Partners, Inc.</span><br>
    NMLS #381760<br>
    www.bluegatelendhub.com
  </address>

  <div class="brand-mark">
    <span class="brand-dot"></span>
    <span class="brand-name">Bluegate Lending Partners, Inc.</span>
  </div>
</main>
</body>
</html>
```